Visit Qalimora Card (School That only teach arabic language) (Guaranteed Payment)

Hi, we are a new school That Teach arabic language in Tunisia, we are looking to conceptulize visit cards for our team. The business card will be printed in color and on Both Sides. We want to communiquer: innovation, excellence, professionalism, leadership and trust. Would we need the business card at the end with the details of everyone of our team (3) General and aussi has one for our center in Tunis. La même designed is used througout of course. Waiting for your sugestions! The address is the Sámi for all the visit cards: 47 Rue des Oliviers Zembra Cedar Building, 3rd Floor 1053 Les Berges du Lac 1, Tunisia aussi la même is the website for all www.qalimora.example The 4 visits Card Those names are: Karim Ouertani Jonas Freiberg Rania Gharbi Qalimora For Karim's Ouertani Visit Card Function name: Managing Partner Phone number: 216 94120386 Email: karim.ouertani@qalimora. example For Rania's visit card function name: Marketing Assistant Phone number: 216 97402615 Email: rania.gharbi@qalimora.example For Jonas's visit card: Function name: Managing Partner Phone number: 49 151 08246519 Mail: @ jonas.freiberg qalimora.example You can find our logo in the attachment.

```html
<!DOCTYPE html>
<html lang="fr">
<head>
<meta charset="utf-8">
<title>Qalimora — cartes de visite</title>
<link rel="stylesheet" href="https://fonts.googleapis.com/css2?family=Lato:wght@400&family=Quicksand:wght@300&display=swap">
<style>
  :root {
    --backdrop: #5d5351;
    --paper: #ffffff;
    --navy: #0b4f8a;
    --orange: #f27c22;
    --sky: #2ec3ec;
    --ink-light: #ffffff;
  }
  * { box-sizing: border-box; margin: 0; padding: 0; }
  html, body { width: 1104px; height: 1200px; overflow: hidden; }
  body { background: var(--backdrop); position: relative; font-family: "Lato", sans-serif; }

  .card {
    position: absolute;
    width: 477px;
    overflow: hidden;
    box-shadow: 4px 6px 10px rgba(0,0,0,0.35);
  }
  .card--front { left: 56px; background: var(--paper); }
  .card--back { left: 571px; }

  .row-1 { top: 66px; height: 272px; }
  .row-2 { top: 467px; height: 271px; }
  .row-3 { top: 868px; height: 245px; }

  .theme-navy { --brand: var(--navy); }
  .theme-orange { --brand: var(--orange); }
  .theme-sky { --brand: var(--sky); }

  .card--back { background: var(--brand); }

  .brand-name {
    position: absolute;
    left: 0; right: 0;
    text-align: center;
    font-family: "Lato", sans-serif;
    font-weight: 400;
    font-size: 54px;
    line-height: 1;
    letter-spacing: 0.5px;
  }
  .card--front .brand-name { color: var(--brand); }
  .card--back .brand-name { color: var(--ink-light); top: 50%; transform: translateY(-55%); }

  .website {
    position: absolute;
    font-family: "Quicksand", sans-serif;
    font-weight: 300;
    line-height: 1;
  }
  .card--front .website {
    left: 0; right: 0;
    text-align: center;
    font-size: 18px;
    color: var(--brand);
  }
  .card--back .website {
    right: 9px; bottom: 6px;
    font-size: 18px;
    color: var(--ink-light);
  }

  .info-band {
    position: absolute;
    left: 0; right: 0; bottom: 0;
    background: var(--brand);
    color: var(--ink-light);
    font-size: 11.5px;
    line-height: 15px;
    display: flex;
    justify-content: space-between;
    align-items: center;
    padding: 0 18px 0 20px;
  }
  .row-1 .info-band, .row-2 .info-band { top: 160px; padding-top: 6px; }
  .row-3 .info-band { top: 132px; padding-top: 4px; }

  .address { text-align: right; }

  .row-1 .card--front .brand-name, .row-1.card--front .brand-name { top: 40px; }
  .row-1.card--front .website, .row-2.card--front .website { top: 104px; }
  .row-2.card--front .brand-name { top: 40px; }
  .row-3.card--front .brand-name { top: 12px; }
  .row-3.card--front .website { top: 76px; }
</style>
</head>
<body>

  <!-- Managing Partner, navy -->
  <section class="card card--front row-1 theme-navy">
    <p class="brand-name">qalimora</p>
    <p class="website">www.qalimora.example</p>
    <div class="info-band">
      <div class="contact">
        <p>Function name : Managing Partner</p>
        <p>Phone number : +216 94 120 386</p>
        <p>Mail : karim.ouertani@qalimora.example</p>
      </div>
      <div class="address">
        <p>47 Rue des Oliviers Zembra</p>
        <p>Immeuble Cèdres, 3ème étage</p>
        <p>1053 Les Berges du Lac 1, Tunisie</p>
      </div>
    </div>
  </section>
  <section class="card card--back row-1 theme-navy">
    <p class="brand-name">qalimora</p>
    <p class="website">www.qalimora.example</p>
  </section>

  <!-- Marketing Assistant, orange -->
  <section class="card card--front row-2 theme-orange">
    <p class="brand-name">qalimora</p>
    <p class="website">www.qalimora.example</p>
    <div class="info-band">
      <div class="contact">
        <p>Function name : Marketing Assistant</p>
        <p>Phone number : +216 97 402 615</p>
        <p>Mail : rania.gharbi@qalimora.example</p>
      </div>
      <div class="address">
        <p>47 Rue des Oliviers Zembra</p>
        <p>Immeuble Cèdres, 3ème étage</p>
        <p>1053 Les Berges du Lac 1, Tunisie</p>
      </div>
    </div>
  </section>
  <section class="card card--back row-2 theme-orange">
    <p class="brand-name">qalimora</p>
    <p class="website">www.qalimora.example</p>
  </section>

  <!-- Managing Partner, sky -->
  <section class="card card--front row-3 theme-sky">
    <p class="brand-name">qalimora</p>
    <p class="website">www.qalimora.example</p>
    <div class="info-band">
      <div class="contact">
        <p>Function name : Managing Partner</p>
        <p>Phone number : +49 151 08 246 519</p>
        <p>Mail : jonas.freiberg@qalimora.example</p>
      </div>
      <div class="address">
        <p>47 Rue des Oliviers Zembra</p>
        <p>Immeuble Cèdres, 3ème étage</p>
        <p>1053 Les Berges du Lac 1, Tunisie</p>
      </div>
    </div>
  </section>
  <section class="card card--back row-3 theme-sky">
    <p class="brand-name">qalimora</p>
    <p class="website">www.qalimora.example</p>
  </section>

</body>
</html>
```